KWI Business Card

Please create a creative design for a business card using the new theme from the Logo & website. This company's main focus is food manufacturing building construction. Please integrate the new logo attached.

Please use the following information for the demo card:

Korvel Walls, Inc.
Dana Whitcombe
dwhitcombe@korvelwalls.example
Cell: 312-555-0178
218 Larkmoor Ave
Fenmore, IL 60418

See pictures and more information on the website.

www.korvelwalls.example

```html
<!DOCTYPE html>
<html lang="en">
<head>
<meta charset="utf-8">
<title>KWI Business Card</title>
<link rel="stylesheet" href="https://fonts.googleapis.com/css2?family=Exo+2:wght@700&family=Roboto:wght@400;700&display=swap">
<style>
  :root {
    --canvas: #262626;
    --card: #141414;
    --card-edge: #1e1e1e;
    --blue: #3b7fd1;
    --blue-light: #8cc2ee;
    --text: #e6e6e6;
  }
  * { box-sizing: border-box; margin: 0; padding: 0; }
  html, body { width: 1200px; height: 1200px; overflow: hidden; background: var(--canvas); }
  body { display: flex; flex-direction: column; align-items: center; justify-content: center; gap: 60px; font-family: "Roboto", sans-serif; }
  .card {
    width: 900px; height: 514px; border-radius: 26px;
    background: radial-gradient(ellipse at 40% 20%, var(--card-edge), var(--card) 70%);
    box-shadow: 0 18px 40px rgba(0,0,0,.55);
    position: relative; display: flex; align-items: center;
  }
  .brand { display: flex; align-items: center; gap: 16px; }
  .brand-mark { width: 22px; height: 22px; background: var(--blue-light); border-radius: 50%; }
  .brand-name { font-family: "Roboto", sans-serif; font-weight: 700; color: var(--blue); letter-spacing: 4px; }
  .card-front { justify-content: center; }
  .card-front .brand-name { font-size: 150px; }
  .card-back { padding: 0 70px; }
  .card-back .brand { width: 340px; justify-content: center; }
  .card-back .brand-name { font-size: 110px; }
  .divider { width: 2px; height: 190px; background: var(--blue); margin: 0 44px 0 30px; }
  .contact { color: var(--text); font-size: 19px; line-height: 1.45; white-space: nowrap; }
  .contact-name { font-family: "Exo 2", sans-serif; font-weight: 700; font-size: 36px; color: var(--blue); letter-spacing: 1px; text-transform: uppercase; margin-bottom: 10px; }
  .contact-company { font-weight: 700; font-size: 22px; color: var(--blue-light); }
  .contact-line { display: flex; align-items: center; gap: 10px; }
  .contact-line svg { width: 18px; height: 18px; flex: none; }
  .contact-line .accent { color: var(--blue-light); font-weight: 700; }
</style>
</head>
<body>
  <section class="card card-front">
    <div class="brand">
      <span class="brand-mark"></span>
      <span class="brand-name">KWI</span>
    </div>
  </section>

  <section class="card card-back">
    <div class="brand">
      <span class="brand-mark"></span>
      <span class="brand-name">KWI</span>
    </div>
    <div class="divider"></div>
    <div class="contact">
      <div class="contact-name">Dana Whitcombe</div>
      <div class="contact-company">Korvel Walls, Inc.</div>
      <div>218 Larkmoor Ave Fenmore, IL 60418</div>
      <div class="contact-line">
        <svg viewBox="0 0 20 20"><circle cx="10" cy="10" r="10" fill="#3b7fd1"/><path d="M7 5.5l2 2-1 1.3a6 6 0 0 0 3.2 3.2l1.3-1 2 2-1.3 1.5C9.5 14 6 10.5 5.5 6.8z" fill="#fff"/></svg>
        <span>312-555-0178</span>
      </div>
      <div class="contact-line">
        <svg viewBox="0 0 20 20"><circle cx="10" cy="10" r="10" fill="#3b7fd1"/><rect x="5" y="6.5" width="10" height="7" rx="1" fill="none" stroke="#fff" stroke-width="1.3"/><path d="M5.3 7l4.7 3.6L14.7 7" fill="none" stroke="#fff" stroke-width="1.3"/></svg>
        <span>dwhitcombe@korvelwalls.example</span>
      </div>
      <div class="contact-line">
        <svg viewBox="0 0 20 20"><circle cx="10" cy="10" r="10" fill="#3b7fd1"/><circle cx="10" cy="10" r="5" fill="none" stroke="#fff" stroke-width="1.2"/><ellipse cx="10" cy="10" rx="2.2" ry="5" fill="none" stroke="#fff" stroke-width="1.1"/><path d="M5 10h10" stroke="#fff" stroke-width="1.1"/></svg>
        <span>www.<span class="accent">korvelwalls</span>.example</span>
      </div>
    </div>
  </section>
</body>
</html>
```